Quietly Meadows needs a brochure

I need to put together a booklet type brochure visually describing what I do. I would like the brochure to have the same elegance as the logo and the business card. I envision using the green design from the back of the business card, on the back of the brochure as well. I would like to have a space for an "About Us" area in which I can explain about the evolution of Quietly Meadows. I would also like to have pictures of work that I have completed. I will send you both copy and photos. I would like the brochure to print matte and be an unusual shape - like a square booklet instead of the normal 8.5x11. I would also like to include the logos of the organizations that I am a member of - NPVO, VORCUS, KREB.
Having some trouble uploading with internet explorer. Will fix the problem and upload ASAP. Thank you all for your patience.

```html
<!DOCTYPE html>
<html lang="en">
<head>
<meta charset="utf-8">
<title>Quietly Meadows – Brochure Panel</title>
<link rel="stylesheet" href="https://fonts.googleapis.com/css2?family=Mulish:wght@400;600;700;800&display=swap">
<style>
  :root {
    --ink: #2b2b2b;
    --body: #3a3a3a;
    --leaf: #8dc63f;
    --leaf-deep: #6fa82c;
    --bark: #8b5a3c;
    --night: #0a0a0a;
    --notice: #c2185b;
    --contact: #8a6457;
    --paper: #ffffff;
  }
  html, body {
    margin: 0;
    padding: 0;
    width: 1200px;
    height: 3600px;
    overflow: hidden;
    background: var(--paper);
  }
  .brochure {
    position: relative;
    width: 1200px;
    height: 3600px;
    overflow: hidden;
    background: var(--paper);
    font-family: "Mulish", "Century Gothic", sans-serif;
    color: var(--body);
  }
  .die-cut-band {
    position: absolute;
    top: 0; left: 0;
    width: 1200px;
    height: 260px;
  }
  .die-cut-note {
    position: absolute;
    top: 36px;
    right: 90px;
    width: 330px;
    margin: 0;
    font-size: 20px;
    line-height: 1.3;
    color: var(--notice);
    text-align: right;
  }
  .brand-mark {
    position: absolute;
    top: 300px;
    left: 80px;
    display: flex;
    align-items: center;
    gap: 18px;
  }
  .brand-mark .brand-dot {
    width: 40px; height: 40px;
    border-radius: 50%;
    background: var(--leaf);
  }
  .brand-mark .brand-name {
    font-size: 52px;
    font-weight: 700;
    color: var(--leaf-deep);
    letter-spacing: 1px;
  }
  .project-photo {
    position: absolute;
    left: 0;
    width: 318px;
    border: 4px solid var(--bark);
    border-left: none;
    border-radius: 0 26px 26px 0;
    box-sizing: border-box;
  }
  .photo-tulips   { top: 495px;  height: 465px; background: linear-gradient(160deg, #6e7a4a 0%, #c2506a 35%, #a98d74 60%, #5a4a3c 100%); }
  .photo-foxglove { top: 1035px; height: 660px; background: linear-gradient(180deg, #7c8a6a 0%, #c89ac4 30%, #3f6a32 55%, #e0a0b8 75%, #d8d070 100%); }
  .photo-planters { top: 1761px; height: 654px; background: linear-gradient(180deg, #8a5a4a 0%, #dfe6d8 25%, #4a5a3a 55%, #2e3228 100%); }
  .copy-block {
    position: absolute;
    left: 366px;
    width: 780px;
  }
  .intro { top: 495px; }
  .intro .lead {
    margin: 0 0 26px;
    font-size: 36px;
    line-height: 1.45;
    font-weight: 700;
    color: var(--ink);
  }
  .intro .standfirst {
    margin: 0;
    font-size: 34px;
    line-height: 1.48;
    color: var(--body);
  }
  .section-title {
    margin: 0 0 14px;
    font-size: 34px;
    font-weight: 800;
    color: var(--leaf);
  }
  .section p {
    margin: 0 0 20px;
    font-size: 28px;
    line-height: 1.5;
  }
  .grow    { top: 1038px; }
  .impress { top: 1840px; }
  .about   { top: 2412px; }
  .garden-scene {
    position: absolute;
    left: 0;
    top: 2940px;
    width: 1200px;
    height: 660px;
    background: linear-gradient(180deg, #ffffff 0%, #f2f8e6 30%, #cfe7a0 62%, #9fd24a 80%, #7bbf2e 100%);
  }
  .footer-brand {
    position: absolute;
    top: 2990px;
    left: 0;
    width: 1200px;
    display: flex;
    justify-content: center;
    align-items: center;
    gap: 14px;
  }
  .footer-brand .brand-dot {
    width: 30px; height: 30px;
    border-radius: 50%;
    background: var(--leaf);
  }
  .footer-brand .brand-name {
    font-size: 40px;
    font-weight: 700;
    color: var(--leaf-deep);
  }
  .contact {
    position: absolute;
    top: 3362px;
    left: 0;
    width: 1200px;
    text-align: center;
    color: var(--contact);
    font-weight: 600;
  }
  .contact p {
    margin: 0 0 8px;
    font-size: 34px;
    letter-spacing: 7px;
  }
</style>
</head>
<body>
<main class="brochure">

  <svg class="die-cut-band" viewBox="0 0 1200 260" preserveAspectRatio="none" aria-hidden="true">
    <path d="M0 0 H1200 V150 C1000 240 820 110 600 150 C380 190 200 90 0 160 Z" fill="var(--night)"/>
  </svg>
  <p class="die-cut-note">This would be cut-out if you do have a die cut leaflet- otherwise green</p>

  <div class="brand-mark">
    <span class="brand-dot"></span>
    <span class="brand-name">Quietly Meadows</span>
  </div>

  <div class="project-photo photo-tulips" role="img" aria-label="Photo of tulips and potted plants on a stone terrace"></div>
  <div class="project-photo photo-foxglove" role="img" aria-label="Photo of a border with pink foxgloves, calla lilies and pansies"></div>
  <div class="project-photo photo-planters" role="img" aria-label="Photo of dark planters overflowing with white flowers against a brick wall"></div>

  <section class="copy-block intro">
    <p class="lead">Lorem ipsum dolor sit amet, consec a brocing elit, sed do eiusmod tempor incididunt ut labore et dolore the am a magna aliqua.</p>
    <p class="standfirst">Ut enim ad minim veniam, quis nostrud exercitation ullamco laboris nisi ut aliquip ex ea commodo consequat. Duis aute irure dolor in reprehenderit in voluptate velit esse cillum dolore eu fugiat nulla pariatur.</p>
  </section>

  <section class="copy-block section grow">
    <h2 class="section-title">Simply designed to grow...</h2>
    <p>Sed ut perspiciatis unde omnis iste natus error sit voluptatem accusantium doloremque laudanxplicabo. Nemo enim ipsam voluptatem quia voluptas sit aspernatur aut odit aut fugit.</p>
    <p>sed quia consequuntur magni dolores eos qui ratione voluptatem sequi nesciunt. Neque porro quisquam est, qui dolorem ipsum quia dolor sit amet, consectetur, adipisci velit, sed quia non numquam eius modi tempora incidunt ut labore et dolore magnam aliquam quaerat voluptatem.</p>
    <p>Ut enim ad minim veniam, quis nostrud exercitation ullamco laboris nisi ut aliquip ex ea commodo consequat. Duis aute irure dolor in reprehenderit in voluptate velit esre eu fugiat nulla pariatur.</p>
    <p>Excepteur sint occaident, sunt in culpa qui officia deserunt mollit anim id est laborum.</p>
  </section>

  <section class="copy-block section impress">
    <h2 class="section-title">Simply designed to Impress...</h2>
    <p>Sed ut perspiciatis unde omnis iste natus error sit voluptatem accusantium doloremque laudanxplicabo.</p>
    <p>Nemo enim ipsam voluptatem quia voluptas sit aspernatur aut odit aut fugit, sed quia consequuntur magni dolores eos qui ratione voluptatem sequi nesciunt. Neque porro quisquam est, qui dolorem ipsum quia dolor sit amet, consectetur, adipisci velit, sed quia non numquam eius modi tempora incidunt ut labore et dolore magnam aliquam quaerat voluptatem.</p>
  </section>

  <section class="copy-block section about">
    <h2 class="section-title">Quietly Meadows by Maren Holloway...</h2>
    <p>Exce occaecat cupidatat non proident, sunt in culpa qui officia deserunt mollit anim id rum.</p>
    <p>Sed ut perspiciatis unde omnis iste natus error sit voluptatem accusantium doloremque laudanxplicabo.</p>
    <p>Nemo enim ipsam voluptatem quia voluptas sit asperni ratione voluptatem sequi nesciunt. Neque pouam est, qui dolorem ipsum quia dolor sit amet, consectetur, adipisci velit, sed quia non numquam eius modi taerat voluptatem.</p>
  </section>

  <div class="garden-scene" role="img" aria-label="Illustration of a gardener with a spade and basket beside a meadow of flowers, leaves and a butterfly on green grass"></div>

  <div class="footer-brand">
    <span class="brand-dot"></span>
    <span class="brand-name">Quietly Meadows</span>
  </div>

  <footer class="contact">
    <p>Phone: 555-014-2263</p>
    <p>Email: quietlymeadows14@mailbox.example</p>
  </footer>

</main>
</body>
</html>
```